Business Card Design Project

Financial planning, Insurance and Real estate - Financial Services company

Contact Information for Business Card

Looking for something simple in design -
Tolverin Equity LLC
Tolverin Wealth Managment

```html
<!DOCTYPE html>
<html lang="en">
<head>
<meta charset="utf-8">
<title>Tolverin Equity LLC – Business Card</title>
<link href="https://fonts.googleapis.com/css2?family=Montserrat:wght@600&display=swap" rel="stylesheet">
<style>
  :root {
    --page-bg: #e9eaec;
    --card-bg: #ffffff;
    --brand-blue: #1a7bbf;
    --watermark: #eef2f8;
  }
  html, body {
    margin: 0;
    padding: 0;
    width: 1200px;
    height: 1000px;
    overflow: hidden;
    background: var(--page-bg);
  }
  .canvas {
    position: relative;
    width: 1200px;
    height: 1000px;
    display: flex;
    align-items: center;
    justify-content: center;
  }
  .business-card {
    position: relative;
    width: 1000px;
    height: 580px;
    background: var(--card-bg);
    border-radius: 36px;
    overflow: hidden;
    box-shadow: 0 10px 30px rgba(0, 0, 0, 0.12);
    font-family: "Montserrat", sans-serif;
  }
  .watermark-mark {
    position: absolute;
    left: -70px;
    top: 150px;
    width: 300px;
    height: 340px;
    border-radius: 50%;
    background: var(--watermark);
  }
  .brand-mark {
    position: absolute;
    right: 90px;
    top: 110px;
    display: flex;
    align-items: center;
    gap: 18px;
    color: var(--brand-blue);
    font-size: 54px;
    font-weight: 600;
  }
  .brand-mark__dot {
    width: 40px;
    height: 40px;
    border-radius: 50%;
    background: var(--brand-blue);
  }
  .company-lines {
    position: absolute;
    left: 70px;
    bottom: 60px;
    margin: 0;
    color: var(--brand-blue);
    font-size: 34px;
    font-weight: 600;
    line-height: 1.3;
    text-transform: uppercase;
    letter-spacing: 0.5px;
  }
  .company-lines span { display: block; }
  .company-lines .indent { padding-left: 30px; }
  .accent-bar {
    position: absolute;
    left: 0;
    bottom: 50px;
    width: 20px;
    height: 90px;
    background: var(--brand-blue);
  }
</style>
</head>
<body>
  <main class="canvas">
    <section class="business-card" aria-label="Tolverin Equity LLC business card">
      <div class="watermark-mark" aria-hidden="true"></div>
      <div class="brand-mark">
        <span class="brand-mark__dot" aria-hidden="true"></span>
        <span class="brand-mark__name">Tolverin</span>
      </div>
      <div class="accent-bar" aria-hidden="true"></div>
      <p class="company-lines">
        <span>Tolverin Equity LLC</span>
        <span class="indent">Tolverin Wealth Managment</span>
      </p>
    </section>
  </main>
</body>
</html>
```